Promotion for a free HTML weather widget

skyvela (http://www.skyvela.example/) is a meteorological service based in Basel, Switzerland.
We offer a free HTML widget that offers weather forecasts for a selected location anywhere on the world for up to seven days (see http://www.skyvela.example/en_GB/weather/forecast/widgetsetup) which can be included in any other website.
To make the widget more popular and well-known, we would like to add a promotional banner for it on our own homepage. The space where the banner will be located is marked red on the attached banner_location.png.
We have received permissions from three websites that are already using our widget to use a screenshot from their website on this banner.
These websites are:
- http://gazette.norlab.example/ (widget is on the bottom of the page)
- http://www.tonvillage.example/
- http://www.valmira.example/
Requirements
Must have
- - Width: 696px
- Height: 150px to 200px
- fits nicely in our website
- uses screenshots of the three aforementioned websites (widget must be visible, other ads on those website must be unrecognisable)
- Text (English) that praises the most important advantages of the widget: it is free to use, worldwide available, easy to integrate, offers valuable weather information to visitors
- Possibility to change the text on our side for translations

```html
<!DOCTYPE html>
<html lang="en">
<head>
<meta charset="utf-8">
<title>skyvela – Basel forecast</title>
<link rel="stylesheet" href="https://fonts.googleapis.com/css2?family=Arimo:wght@400;700&family=Open+Sans:wdth,wght@75..100,700..800&display=swap">
<style>
:root{
  --bg:#f2f2f2;
  --panel:#ffffff;
  --border:#c9c9c9;
  --tabbar:#3b4a5c;
  --text:#222;
  --muted:#8a8a8a;
  --link:#2a6fc9;
  --sky:#1b3a78;
  --t-yellow:#ffee00;
  --t-orange:#ffa500;
  --t-red:#ff5a00;
  --t-deep:#ff4000;
  --bar:#a9c8ec;
  --heading-bg:#f0f0f0;
  --banner-head:#f0c8c8;
  --rain:#29c4e8;
  --font:"Arimo", Arial, sans-serif;
}
*{box-sizing:border-box;margin:0;padding:0}
html,body{width:783px;height:1200px;overflow:hidden;background:var(--bg)}
body{font-family:var(--font);color:var(--text)}
.page{position:relative;width:724px;height:1110px;transform:scale(1.0815);transform-origin:0 0}
.abs{position:absolute}

.tabbar{left:0;top:0;width:724px;height:20px;background:var(--tabbar);display:flex}
.tab{flex:1;display:flex;align-items:center;gap:8px;padding-left:22px;border-right:1px solid #2d3946}
.tab:first-child{background:#fff}
.tab .dot{width:12px;height:12px;border-radius:50%;border:2px solid #fff}
.tab:first-child .dot{border-color:#333}
.tab .meter{width:56px;height:6px;background:#8a95a3;position:relative}
.tab .meter i{position:absolute;left:0;top:0;height:6px;background:#f2d400}
.tab:first-child .meter{background:#3fb000}

.panel{position:absolute;left:14px;width:698px;background:var(--panel);border:1px solid var(--border)}
.forecast{top:20px;height:412px;border-top:none}

.sunmoon{left:10px;top:36px;display:flex;gap:6px;align-items:center;font-size:12px}
.uv{width:42px;height:42px;background:var(--sky);display:flex;color:#fff;font-weight:700}
.uv .lbl{width:16px;background:#1a2f63;display:flex;flex-direction:column;align-items:center;font-size:11px;line-height:12px;padding-top:2px}
.uv .lbl b{color:#ff3030;font-size:14px;margin-top:4px}
.times{line-height:20px}
.moonbox{width:42px;height:42px;background:#000}

.row{position:absolute;left:10px;width:690px;display:flex;align-items:center;font-size:14px}
.row .label{width:276px}
.row .cell{width:58px;text-align:center}
.row.blue .label,.row.blue .cell{color:var(--link)}
.hours{top:12px}
.icons{top:36px}
.icon{width:44px;height:44px;margin:0 7px;background:var(--sky)}
.temp .cell span{display:inline-block;width:46px;height:28px;line-height:28px;font-weight:700;border:1px solid #aaa;font-size:14px}
.y{background:var(--t-yellow)}.o{background:var(--t-orange)}.r{background:var(--t-red)}.d{background:var(--t-deep)}
.spot .cell svg{width:48px;height:42px;border:1px solid #777;background:#fff}
.spotlabel small{display:block;font-size:10px}

.tools{left:10px;top:348px;width:356px;height:20px;background:var(--bar);border-radius:0 10px 10px 0;display:flex;color:#fff;font-size:14px}
.tools div{display:flex;align-items:center;gap:6px;padding-left:4px}
.tools div:first-child{width:222px}
.tools i{width:14px;height:14px;background:#fff;display:inline-block}
.help{left:10px;top:382px;display:flex;font-size:14px;color:var(--muted)}
.help div{display:flex;align-items:center;gap:8px}
.help div:nth-child(1){width:222px}
.help div:nth-child(2){width:222px}
.help i{width:18px;height:18px;background:#aaa;display:inline-block;border-radius:2px}

.head{position:absolute;left:0;top:0;width:100%;height:30px;background:var(--heading-bg);border-bottom:1px solid #ddd;font-weight:700;font-size:19px;line-height:30px;padding-left:10px}
.radar{top:442px;height:244px}
.map{background:linear-gradient(160deg,#cfd6de,#b7c1cc 50%,#d5dbe2);border:1px solid #aaa}
.map-big{left:10px;top:46px;width:188px;height:182px}
.map-small{left:232px;top:78px;width:122px;height:128px}
.stamp{position:absolute;background:#fff;font-size:10px;font-weight:700;color:#1b3a78;padding:0 3px}
.radar .title{left:232px;top:46px;font-size:15px}
.radar .info{left:374px;top:80px;width:304px;font-size:14px;line-height:21px}
.radar .info b{color:var(--link)}
.radar .info span{display:block;margin-top:6px}
.radar .more{left:374px;top:206px;font-size:14px;color:var(--muted);display:flex;gap:8px;align-items:center}
.radar .more i{width:18px;height:18px;background:#aaa;display:inline-block}

.banner-wrap{top:696px;height:183px}
.banner-wrap .head{background:var(--banner-head);color:#333}
.banner{left:0;top:31px;width:696px;height:150px;background:radial-gradient(ellipse at 62% 45%,#d8e4ee 0%,#9cc3e0 28%,#5e9fd1 55%,#2f78b8 100%)}
.badge{left:8px;top:30px;width:86px;height:90px;background:#fff;border-radius:6px;display:flex;align-items:center;justify-content:center}
.badge .brand{font-family:var(--font);font-weight:700;font-size:17px;color:var(--sky)}
.claims{left:124px;top:14px;list-style:none;font-family:"Open Sans",sans-serif;font-weight:800;font-stretch:80%;font-size:19px;color:#fff;text-shadow:1px 1px 0 #1b3a78,-1px 0 0 #1b3a78,0 1px 2px #0b2a50}
.claims li{height:35px;line-height:24px}

.meteo{top:888px;height:222px}
.meteo svg{position:absolute;left:0;top:30px}
</style>
</head>
<body>
<div class="page">

  <nav class="tabbar abs">
    <div class="tab"><span class="dot"></span><span class="meter"></span></div>
    <div class="tab"><span class="dot"></span><span class="meter"><i style="width:30px"></i></span></div>
    <div class="tab"><span class="dot"></span><span class="meter"><i style="width:30px"></i></span></div>
    <div class="tab"><span class="dot"></span><span class="meter"><i style="width:22px;background:#ffa500"></i></span></div>
    <div class="tab"><span class="dot"></span><span class="meter"><i style="width:30px"></i></span></div>
    <div class="tab"><span class="dot"></span><span class="meter"><i style="width:30px"></i></span></div>
    <div class="tab"><span class="dot"></span><span class="meter"><i style="width:36px;background:#9bd13a"></i></span></div>
  </nav>

  <section class="panel forecast">
    <div class="row hours"><span class="label">Monday, 05.08 (CEST)</span>
      <span class="cell">05:00</span><span class="cell">08:00</span><span class="cell">11:00</span><span class="cell">14:00</span><span class="cell">17:00</span><span class="cell">20:00</span><span class="cell">23:00</span></div>

    <div class="abs sunmoon">
      <div class="uv"><div class="lbl">UV<b>8</b></div><svg width="26" height="42"><circle cx="13" cy="21" r="8" fill="#fff"/></svg></div>
      <div class="times">↑06:15<br>↓20:55</div>
      <div class="moonbox"></div>
      <div class="times">↑04:52<br>↓19:45</div>
    </div>

    <div class="row icons"><span class="label"></span>
      <svg class="icon" viewBox="0 0 44 44"><path d="M26 10a12 12 0 1 0 6 20 10 10 0 0 1-6-20z" fill="#f4e7a0"/></svg>
      <svg class="icon" viewBox="0 0 44 44"><circle cx="22" cy="24" r="9" fill="#ffc400"/></svg>
      <svg class="icon" viewBox="0 0 44 44"><path d="M6 10h30M10 15h26" stroke="#c8d6ea" stroke-width="3"/><circle cx="22" cy="26" r="8" fill="#ffc400"/></svg>
      <svg class="icon" viewBox="0 0 44 44"><path d="M6 10h30M10 15h26" stroke="#c8d6ea" stroke-width="3"/><circle cx="22" cy="26" r="8" fill="#ffc400"/></svg>
      <svg class="icon" viewBox="0 0 44 44"><path d="M6 10h30M10 15h26" stroke="#c8d6ea" stroke-width="3"/><circle cx="22" cy="26" r="8" fill="#ffc400"/></svg>
      <svg class="icon" viewBox="0 0 44 44"><path d="M6 10h30M10 15h26" stroke="#c8d6ea" stroke-width="3"/><circle cx="22" cy="26" r="8" fill="#ffb000"/></svg>
      <svg class="icon" viewBox="0 0 44 44"><ellipse cx="24" cy="22" rx="12" ry="7" fill="#b8bcc6"/><path d="M22 28l-3 8 5-3-2 7" stroke="#ff3aa0" stroke-width="2" fill="none"/></svg>
    </div>

    <div class="row temp" style="top:90px"><span class="label">Temperature (°C)</span>
      <span class="cell"><span class="y">19 °</span></span><span class="cell"><span class="y">19 °</span></span><span class="cell"><span class="o">25 °</span></span><span class="cell"><span class="r">29 °</span></span><span class="cell"><span class="d">32 °</span></span><span class="cell"><span class="d">31 °</span></span><span class="cell"><span class="o">27 °</span></span></div>
    <div class="row" style="top:128px"><span class="label">Temperature felt (°C)</span><span class="cell">21°</span><span class="cell">20°</span><span class="cell">25°</span><span class="cell">33°</span><span class="cell">35°</span><span class="cell">34°</span><span class="cell">32°</span></div>
    <div class="row" style="top:155px"><span class="label">Wind direction</span>
      <span class="cell">↖</span><span class="cell">↖</span><span class="cell">↖</span><span class="cell">←</span><span class="cell">←</span><span class="cell">↖</span><span class="cell">↑</span></div>
    <div class="row" style="top:182px"><span class="label">Wind speed (km/h)</span><span class="cell">7</span><span class="cell">9</span><span class="cell">13</span><span class="cell">11</span><span class="cell">11</span><span class="cell">10</span><span class="cell">5</span></div>
    <div class="row" style="top:208px"><span class="label">Wind gusts (km/h)</span><span class="cell">8</span><span class="cell">15</span><span class="cell">15</span><span class="cell">11</span><span class="cell">25</span><span class="cell">27</span><span class="cell">6</span></div>
    <div class="row blue" style="top:234px"><span class="label">Precipitation (mm)</span><span class="cell">-</span><span class="cell">-</span><span class="cell">-</span><span class="cell">-</span><span class="cell">-</span><span class="cell">-</span><span class="cell">-</span></div>
    <div class="row blue" style="top:260px"><span class="label">Precipitation probability</span><span class="cell">0%</span><span class="cell">0%</span><span class="cell">0%</span><span class="cell">1%</span><span class="cell">17%</span><span class="cell">14%</span><span class="cell">19%</span></div>

    <div class="row spot" style="top:286px"><span class="label spotlabel">dropZONE<small>Precipitation distribution within 15 km</small></span>
      <span class="cell"><svg viewBox="0 0 48 42"><g fill="none" stroke="#555"><circle cx="24" cy="21" r="18"/><circle cx="24" cy="21" r="12"/><circle cx="24" cy="21" r="6"/></g></svg></span>
      <span class="cell"><svg viewBox="0 0 48 42"><g fill="none" stroke="#555"><circle cx="24" cy="21" r="18"/><circle cx="24" cy="21" r="12"/><circle cx="24" cy="21" r="6"/></g></svg></span>
      <span class="cell"><svg viewBox="0 0 48 42"><g fill="none" stroke="#555"><circle cx="24" cy="21" r="18"/><circle cx="24" cy="21" r="12"/><circle cx="24" cy="21" r="6"/></g></svg></span>
      <span class="cell"><svg viewBox="0 0 48 42"><g fill="none" stroke="#555"><circle cx="24" cy="21" r="18"/><circle cx="24" cy="21" r="12"/><circle cx="24" cy="21" r="6"/></g></svg></span>
      <span class="cell"><svg viewBox="0 0 48 42"><path d="M6 26h8v8H6z" fill="var(--rain)"/><g fill="none" stroke="#555"><circle cx="24" cy="21" r="18"/><circle cx="24" cy="21" r="12"/><circle cx="24" cy="21" r="6"/></g></svg></span>
      <span class="cell"><svg viewBox="0 0 48 42"><path d="M24 12h8v10h-8zM8 26h10v8H8z" fill="var(--rain)"/><g fill="none" stroke="#555"><circle cx="24" cy="21" r="18"/><circle cx="24" cy="21" r="12"/><circle cx="24" cy="21" r="6"/></g></svg></span>
      <span class="cell"><svg viewBox="0 0 48 42"><path d="M6 3h36v14H6z" fill="var(--rain)"/><g fill="none" stroke="#555"><circle cx="24" cy="21" r="18"/><circle cx="24" cy="21" r="12"/><circle cx="24" cy="21" r="6"/></g></svg></span>
    </div>

    <div class="abs tools"><div><i></i>Additional parameters</div><div><i></i>Detail</div></div>
    <div class="abs help"><div><i></i>Show help</div><div><i></i>Bookmark this page</div><div><i></i>Share on Pagebook</div></div>
  </section>

  <section class="panel radar">
    <h2 class="head">Precipitation radar with lightning</h2>
    <div class="abs map map-big" role="img" aria-label="Radar map of Switzerland with city markers"><span class="stamp" style="right:2px;top:2px">Mon 12:10</span><span class="stamp" style="right:2px;bottom:2px;background:#1b3a78;color:#fff;font-weight:400">skyvela.example</span></div>
    <p class="abs title">Local short-term precipitation forecast</p>
    <div class="abs map map-small" role="img" aria-label="Local radar map centred on Basel"><span class="stamp" style="left:40px;top:0;background:#000;color:#fff;font-weight:400">05.08 12:25</span></div>
    <p class="abs info"><b>0 mm</b> Precipitation in Basel at 11:30-12:40<span>The animation shows the distribution of precipitation for the next hour. Lightning of the past half hour is displayed as red crosses. Basel is located in the center.</span></p>
    <div class="abs more"><i></i>Show help</div>
  </section>

  <section class="panel banner-wrap">
    <h2 class="head">Your banner here</h2>
    <div class="abs banner" role="img" aria-label="Sky with large cumulus cloud">
      <div class="abs badge"><span class="brand">skyvela</span></div>
      <ul class="abs claims">
        <li>it is free to use</li>
        <li>worldwide available</li>
        <li>easy to integrate</li>
        <li>offers valuable weather information to visitors</li>
      </ul>
    </div>
  </section>

  <section class="panel meteo">
    <h2 class="head">Meteogram - 5 days - Basel</h2>
    <svg width="698" height="192" viewBox="0 0 698 192" font-family="Arimo, Arial, sans-serif">
      <text x="2" y="38" font-size="10" font-weight="700" fill="#1b3a78">47.57°N / 7.60°E (263m asl)</text>
      <text x="686" y="26" font-size="16" fill="#888" text-anchor="end">skyvela</text>
      <g font-size="12" font-weight="700" text-anchor="middle" fill="#222">
        <text x="108" y="50">05.08</text><text x="108" y="63">Monday</text>
        <text x="226" y="50">06.08</text><text x="226" y="63">Tuesday</text>
        <text x="345" y="50">07.08</text><text x="345" y="63">Wednesday</text>
        <text x="463" y="50">08.08</text><text x="463" y="63">Thursday</text>
        <text x="582" y="50">09.08</text><text x="582" y="63">Friday</text>
      </g>
      <rect x="50" y="74" width="590" height="106" fill="#f4f4f4"/>
      <g fill="#f4f38a"><rect x="80" y="74" width="90" height="106"/><rect x="198" y="74" width="90" height="106"/><rect x="316" y="74" width="90" height="106"/><rect x="434" y="74" width="90" height="106"/><rect x="552" y="74" width="88" height="106"/></g>
      <rect x="50" y="148" width="590" height="32" fill="#2fa84a"/>
      <rect x="50" y="140" width="590" height="8" fill="#9ad14a"/>
      <path d="M50 140 C70 140 80 130 100 110 S130 90 140 100 S180 138 200 130 S230 100 240 108 S280 138 310 136 S350 110 370 114 S420 140 440 136 S480 120 490 124 S530 146 550 140 S590 118 610 124 S630 136 640 136 L640 140 L50 140Z" fill="#ffd400"/>
      <path d="M50 140 C70 140 80 130 100 110 S130 90 140 100 S180 138 200 130 S230 100 240 108 S280 138 310 136 S350 110 370 114 S420 140 440 136 S480 120 490 124 S530 146 550 140 S590 118 610 124 S630 136 640 136" fill="none" stroke="#ff4000" stroke-width="2.5"/>
      <g font-size="12" font-weight="700" text-anchor="middle"><text x="138" y="115">32</text><text x="252" y="127">31</text><text x="365" y="131">28</text><text x="488" y="142">24</text><text x="607" y="142">24</text>
        <g fill="#1b3a9a"><text x="210" y="149">22</text><text x="328" y="154">20</text><text x="432" y="158">19</text><text x="546" y="166">16</text></g></g>
      <g font-size="12" fill="#ff4000" text-anchor="end"><text x="46" y="83">40</text><text x="46" y="99">35</text><text x="46" y="114">30</text><text x="46" y="130">25</text><text x="46" y="145">20</text><text x="46" y="161">15</text><text x="46" y="176">10</text></g>
      <g font-size="12" fill="#ff4000"><text x="646" y="83">40</text><text x="646" y="99">35</text><text x="646" y="114">30</text><text x="646" y="130">25</text><text x="646" y="145">20</text><text x="646" y="161">15</text><text x="646" y="176">10</text></g>
      <text x="10" y="150" font-size="12" fill="#ff4000" transform="rotate(-90 10 150)">Temp. (°C)</text>
      <g fill="#ffc400"><circle cx="108" cy="96" r="6"/><circle cx="146" cy="84" r="6"/><circle cx="232" cy="98" r="5"/><circle cx="340" cy="110" r="5"/><circle cx="500" cy="106" r="5"/><circle cx="620" cy="110" r="5"/></g>
      <g font-size="11" font-weight="700" fill="#222" text-anchor="middle">
        <text x="50" y="194">Mon</text><text x="80" y="194">6</text><text x="110" y="194">12</text><text x="140" y="194">18</text>
        <text x="168" y="194">Tue</text><text x="198" y="194">6</text><text x="228" y="194">12</text><text x="258" y="194">18</text>
        <text x="286" y="194">Wed</text><text x="316" y="194">6</text><text x="346" y="194">12</text><text x="376" y="194">18</text>
        <text x="404" y="194">Thu</text><text x="434" y="194">6</text><text x="464" y="194">12</text><text x="494" y="194">18</text>
        <text x="522" y="194">Fri</text><text x="552" y="194">6</text><text x="582" y="194">12</text><text x="612" y="194">18</text>
        <text x="640" y="194">Sat</text><text x="674" y="194">(CEST)</text>
      </g>
    </svg>
  </section>

</div>
</body>
</html>
```